Need a book cover design for a Lumora Book

Book has a long title and sub title so lots of words to fit on the cover.

I can be flexible a bit with the sub title due to the length of it but ideally i can get a design that takes everything.

Here is the title:

Tidal Geology: The Roots of Erosion, Sedimentation, and Canyon Forming

Sub Title/Heading
An Easy Primer on Coastal Cliffs, Dune Drift, River Beds, and Delta Mapping Methods

```html
<!DOCTYPE html>
<html lang="en">
<head>
<meta charset="utf-8">
<title>Tidal Geology — Book Cover</title>
<link rel="stylesheet" href="https://fonts.googleapis.com/css2?family=Questrial&display=swap">
<style>
  :root {
    --page: #ffffff;
    --sun: #fcd008;
    --amber: #f9b22c;
    --tangerine: #f2884a;
    --coral: #ee6250;
    --crimson: #e61b50;
    --ink-light: #ffffff;
  }
  * { margin: 0; padding: 0; box-sizing: border-box; }
  html, body {
    width: 1200px;
    height: 900px;
    overflow: hidden;
    background: var(--page);
  }
  .canvas {
    position: relative;
    width: 1200px;
    height: 900px;
  }
  .book-cover {
    position: absolute;
    left: 341px;
    top: 50px;
    width: 571px;
    height: 808px;
    overflow: hidden;
    font-family: "Questrial", "Century Gothic", sans-serif;
    color: var(--ink-light);
    background: linear-gradient(
      to bottom,
      var(--sun) 0%,
      var(--sun) 38%,
      var(--amber) 58%,
      var(--tangerine) 80%,
      var(--coral) 92%,
      var(--crimson) 100%
    );
  }
  .cover-artwork {
    position: absolute;
    left: 188px;
    top: 90px;
    width: 195px;
    height: 627px;
    background: linear-gradient(
      to bottom,
      rgba(230, 27, 80, 0.55) 0%,
      rgba(242, 136, 74, 0.35) 40%,
      rgba(252, 208, 8, 0) 75%
    );
  }
  .title-block {
    position: absolute;
    left: 0;
    right: 0;
    top: 355px;
    text-align: center;
  }
  .book-title {
    font-size: 46px;
    font-weight: 400;
    letter-spacing: 0.5px;
    line-height: 1;
    -webkit-text-stroke: 1px var(--ink-light);
  }
  .book-subtitle {
    margin-top: 10px;
    font-size: 20px;
    font-weight: 400;
    line-height: 23px;
  }
  .series-blurb {
    position: absolute;
    left: 27px;
    top: 700px;
    width: 150px;
    font-size: 13px;
    line-height: 14.6px;
  }
  .author-name {
    position: absolute;
    right: 27px;
    top: 713px;
    font-size: 12.5px;
    -webkit-text-stroke: 0.3px var(--ink-light);
  }
</style>
</head>
<body>
  <main class="canvas">
    <section class="book-cover">
      <div class="cover-artwork" role="img" aria-label="Abstract cover artwork: a tall soft form fading from crimson at the top to sunny yellow below"></div>

      <header class="title-block">
        <h1 class="book-title">TIDAL GEOLOGY</h1>
        <p class="book-subtitle">The Roots of Erosion,<br>Sedimentation, and<br>Canyon Forming</p>
      </header>

      <p class="series-blurb">An Easy Primer on Coastal Cliffs, Dune Drift, River Beds, and Delta Mapping Methods</p>

      <p class="author-name">Authors Name(s)</p>
    </section>
  </main>
</body>
</html>
```